Northfield Server Crate requires an Email Marketing Design template

Northfield Server Crate are a rapidly expanding UK based internet hosting company that have just re-branded through Craft Lantern.
We provide internet based services such as website hosting, dedicated and managed servers, domain names as well as email solutions to name a few. We pride ourselves on being able to provide a comprehensive, secure, future proofed and scalable platform for our clients to communicate and do business on.
Northfield Server Crate are looking to go live with a new website on 1st August. In preparation for this we would like to have an HTML Email Template designed for our launch!
We are also having a really big push on the reseller market allowing potential resellers and their end users to manage their own services via a consolidated portal with many features and functions that will grow over time.

Target Market(s)
We have 3 core target markets, the end user who would be the likes of web designers or developers. A reseller market who would want to resell our hosted services and the final target market would be a business client that would want high end server and hosting solutions.
Industry/Entity Type
Internet Service Provider
Requirements
Must have
- To ensure it is inline with the new brand (see attached files).

```html
<!DOCTYPE html>
<html lang="en">
<head>
<meta charset="utf-8">
<title>Northfield Server Crate – Launch Email</title>
<link rel="stylesheet" href="https://fonts.googleapis.com/css2?family=Oswald:wght@400;500;600&family=Open+Sans:wght@400;600;700&display=swap">
<style>
:root{
  --teal:#1fc1c9;
  --mint:#5fc9a6;
  --navy:#18202d;
  --footer:#141b27;
  --red:#e2311f;
  --ink:#2b2f36;
  --grey:#6c7078;
  --rule:#e4e6e9;
  --white:#ffffff;
  --why-1:#86dbe0;
  --why-2:#3ec7cf;
  --why-3:#1ab0ba;
  --why-4:#14979f;
  --why-5:#0c7d88;
}
*{box-sizing:border-box;margin:0;padding:0}
html,body{width:1200px;height:4784px;overflow:hidden;background:var(--white)}
body{font-family:"Open Sans",Arial,sans-serif;color:var(--ink);position:relative}
.heading{font-family:"Oswald","Arial Narrow",sans-serif;text-transform:uppercase;font-weight:500}
a{text-decoration:none}

/* header */
.site-header{position:absolute;left:0;top:0;width:1200px;height:168px;border-bottom:6px solid var(--teal)}
.brand{position:absolute;left:56px;top:40px;display:flex;align-items:center;gap:20px}
.brand-dot{width:76px;height:76px;border-radius:50%;background:var(--teal)}
.brand-name{font-family:"Oswald","Arial Narrow",sans-serif;font-weight:500;font-size:38px;line-height:1.1;color:var(--ink);width:300px}
.call-us{position:absolute;right:28px;top:30px;font-family:"Oswald","Arial Narrow",sans-serif;font-size:22px;font-weight:500;color:var(--ink);letter-spacing:.5px;white-space:nowrap}
.call-us span{color:var(--red)}
.social{display:flex;gap:10px}
.social i{display:block;width:42px;height:42px;border-radius:50%;border:3px solid #b9bdc3}
.site-header .social{position:absolute;right:28px;top:80px}

/* hero */
.hero{position:absolute;left:0;top:168px;width:1200px;height:656px;overflow:hidden}
.hero-photo{position:absolute;inset:0;background:linear-gradient(110deg,#cfd6dc 0%,#b9a58e 38%,#d8c7b3 60%,#8e9aa5 100%)}
.hero-title{position:absolute;left:32px;top:104px;color:var(--white);font-family:"Oswald","Arial Narrow",sans-serif;font-weight:500;text-transform:uppercase;line-height:.95}
.hero-title .small{font-size:54px;display:block}
.hero-title .big{font-size:92px;display:block}
.btn{display:inline-block;font-family:"Oswald","Arial Narrow",sans-serif;text-transform:uppercase;color:var(--white);text-align:center;white-space:nowrap}
.hero .btn{position:absolute;top:536px;height:80px;line-height:80px;font-size:30px;background:var(--teal)}
.hero .btn-plan{left:32px;width:220px}
.hero .btn-contact{left:280px;width:260px}
.price-badge{position:absolute;left:885px;top:402px;width:315px;height:254px;background:var(--red);clip-path:polygon(24% 0,100% 0,100% 100%,0 100%,0 30%);color:var(--white);font-family:"Oswald","Arial Narrow",sans-serif;text-transform:uppercase;white-space:nowrap}
.price-badge .only{position:absolute;left:40px;top:104px;font-size:34px;line-height:1}
.price-badge .amount{position:absolute;left:128px;top:24px;font-size:118px;line-height:1}
.price-badge .amount sup{font-size:54px;vertical-align:top;position:relative;top:10px}
.price-badge .period{position:absolute;left:40px;top:162px;font-size:58px;line-height:1}

/* welcome */
.welcome{position:absolute;left:0;top:824px;width:1200px;height:420px;text-align:center}
.welcome h1{margin-top:86px;font-size:48px;color:var(--ink)}
.welcome p{width:1080px;margin:24px auto 0;font-size:22px;line-height:46px;color:var(--grey)}

/* plans */
.plans{position:absolute;left:20px;top:1244px;width:1164px;display:grid;grid-template-columns:570px 570px;gap:14px 24px}
.plan{position:relative;height:470px;background:var(--navy);color:var(--white)}
.plan h2{position:absolute;left:32px;top:30px;font-size:48px;line-height:1.05;color:var(--white);width:220px}
.plan .from{position:absolute;right:32px;top:32px;text-align:right;font-size:20px}
.plan .from strong{display:block;font-family:"Oswald","Arial Narrow",sans-serif;font-weight:500;color:var(--mint);font-size:56px;line-height:1.1}
.plan .from small{font-size:20px;color:var(--white);font-family:"Open Sans",Arial,sans-serif}
.plan p{position:absolute;left:32px;top:188px;width:506px;font-size:22px;line-height:40px}
.plan .actions{position:absolute;left:32px;top:384px;display:flex;gap:20px}
.plan .btn{height:48px;line-height:48px;font-size:22px;padding:0 20px}
.btn-order{background:var(--teal)}
.btn-info{background:var(--mint)}

/* why choose us */
.why{position:absolute;left:0;top:2220px;width:1200px;height:492px}
.why h2{position:absolute;top:56px;width:100%;text-align:center;font-size:48px}
.why-strip{position:absolute;left:0;top:148px;width:1200px;height:344px;display:flex}
.why-item{flex:1;position:relative;color:var(--white);padding:96px 0 0 32px}
.why-item svg{display:block;width:50px;height:50px;margin-bottom:34px}
.why-item span{font-family:"Oswald","Arial Narrow",sans-serif;text-transform:uppercase;font-size:26px;line-height:1.15;display:block}
.why-item:nth-child(1){background:var(--why-1)}
.why-item:nth-child(2){background:var(--why-2)}
.why-item:nth-child(3){background:var(--why-3)}
.why-item:nth-child(4){background:var(--why-4)}
.why-item:nth-child(5){background:var(--why-5)}

/* blog */
.blog{position:absolute;left:0;top:2712px;width:1200px;height:1308px}
.blog h2{position:absolute;top:70px;width:100%;text-align:center;font-size:48px}
.post{position:absolute;left:52px;width:1096px;height:379px;border-bottom:3px solid var(--rule)}
.post-1{top:186px}
.post-2{top:628px}
.post-3{top:1058px;border-bottom:none;height:250px}
.post-image{position:absolute;left:0;top:0;width:340px;height:240px;background:linear-gradient(120deg,#2c5d86 0%,#6fb3d6 45%,#e9f3f8 70%,#c88bbd 100%)}
.post-body{position:absolute;left:502px;top:0;width:594px}
.post-date{display:flex;align-items:center;gap:14px;font-size:19px;color:var(--grey);height:30px}
.post-date svg{width:24px;height:24px}
.post h3{margin-top:4px;font-size:26px;line-height:36px;font-weight:700;color:var(--ink)}
.post .author{margin-top:4px;font-size:21px;line-height:30px;color:var(--teal)}
.post p{margin-top:8px;font-size:20.5px;line-height:32px;color:var(--grey)}

/* footer */
.site-footer{position:absolute;left:0;top:4020px;width:1200px;height:764px;background:var(--footer);color:var(--white);text-align:center}
.site-footer h2{margin-top:84px;font-size:48px;color:var(--white)}
.address{margin-top:26px;font-size:22px;line-height:38px;color:#d5d8dc}
.footer-phone{margin-top:30px;font-family:"Oswald","Arial Narrow",sans-serif;font-size:80px;line-height:1;color:var(--mint)}
.footer-email{margin-top:4px;font-size:24px;color:var(--teal)}
.site-footer .social{justify-content:center;margin-top:56px}
.site-footer .social i{width:50px;height:50px}
.copyright{margin-top:26px;font-size:21px;line-height:36px;color:#c7cacf}
</style>
</head>
<body>

<header class="site-header">
  <div class="brand">
    <span class="brand-dot"></span>
    <span class="brand-name">Northfield Server Crate</span>
  </div>
  <div class="call-us">CALL US TODAY : <span>0800 555 0142</span></div>
  <div class="social" aria-label="Social links"><i></i><i></i><i></i></div>
</header>

<section class="hero">
  <div class="hero-photo" role="img" aria-label="Photo of a smiling couple using a tablet together at home"></div>
  <h1 class="hero-title"><span class="small">Advanced</span><span class="big">Web Hosting</span></h1>
  <a class="btn btn-plan">Hosting Plan</a>
  <a class="btn btn-contact">Contact Now</a>
  <div class="price-badge">
    <span class="only">Only</span>
    <span class="amount"><sup>$</sup>99</span>
    <span class="period">Per Month</span>
  </div>
</section>

<section class="welcome">
  <h1 class="heading">Welcome to Northfield Server Crate</h1>
  <p>In publishing and graphic design, lorem ipsum is a filler text commonly used to demonstrate the graphic elements of a document or visual presentation. Replacing meaningful content with placeholder text allows viewers to focus on graphic aspects such as font, typography, and page layout without being distracted by the content.</p>
</section>

<section class="plans">
  <article class="plan">
    <h2 class="heading">Web Hosting</h2>
    <div class="from">From only<strong>£49 <small>p/m</small></strong></div>
    <p>In publishing and graphic design, lorem ipsum is a filler text commonly used to demonstrate the graphic elements of a document or visual presentation.</p>
    <div class="actions"><a class="btn btn-order">Order Now</a><a class="btn btn-info">More Info</a></div>
  </article>
  <article class="plan">
    <h2 class="heading">Dedicated Server</h2>
    <div class="from">From only<strong>£39 <small>p/m</small></strong></div>
    <p>In publishing and graphic design, lorem ipsum is a filler text commonly used to demonstrate the graphic elements of a document or visual presentation.</p>
    <div class="actions"><a class="btn btn-order">Order Now</a><a class="btn btn-info">More Info</a></div>
  </article>
  <article class="plan">
    <h2 class="heading">Domain Name</h2>
    <div class="from">From only<strong>£29 <small>p/m</small></strong></div>
    <p>In publishing and graphic design, lorem ipsum is a filler text commonly used to demonstrate the graphic elements of a document or visual presentation.</p>
    <div class="actions"><a class="btn btn-order">Order Now</a><a class="btn btn-info">More Info</a></div>
  </article>
  <article class="plan">
    <h2 class="heading">VPS</h2>
    <div class="from">From only<strong>£19 <small>p/m</small></strong></div>
    <p>In publishing and graphic design, lorem ipsum is a filler text commonly used to demonstrate the graphic elements of a document or visual presentation.</p>
    <div class="actions"><a class="btn btn-order">Order Now</a><a class="btn btn-info">More Info</a></div>
  </article>
</section>

<section class="why">
  <h2 class="heading">Why Choose Us?</h2>
  <div class="why-strip">
    <div class="why-item">
      <svg viewBox="0 0 50 50"><circle cx="25" cy="25" r="22" fill="none" stroke="#fff" stroke-width="3"/><text x="25" y="31" text-anchor="middle" font-family="Oswald,sans-serif" font-size="17" fill="#fff">24</text></svg>
      <span>Free 24x7<br>Support</span>
    </div>
    <div class="why-item">
      <svg viewBox="0 0 50 50"><rect x="6" y="4" width="24" height="30" fill="none" stroke="#fff" stroke-width="3"/><rect x="20" y="16" width="24" height="30" fill="#fff"/></svg>
      <span>Free<br>Migration</span>
    </div>
    <div class="why-item">
      <svg viewBox="0 0 50 50"><circle cx="25" cy="25" r="22" fill="none" stroke="#fff" stroke-width="3"/><text x="25" y="33" text-anchor="middle" font-family="Open Sans,sans-serif" font-size="22" font-weight="700" fill="#fff">£</text></svg>
      <span>No Hidden<br>Charges</span>
    </div>
    <div class="why-item">
      <svg viewBox="0 0 50 50"><path d="M25 4 L46 24 H40 V46 H29 V33 H21 V46 H10 V24 H4 Z" fill="#fff"/></svg>
      <span>Gret Value<br>Domain Name</span>
    </div>
    <div class="why-item">
      <svg viewBox="0 0 50 50"><path d="M25 45 C8 32 3 24 3 15 C3 8 9 3 15 3 C20 3 23 6 25 10 C27 6 30 3 35 3 C41 3 47 8 47 15 C47 24 42 32 25 45 Z" fill="#fff"/></svg>
      <span>Our Customer<br>Love Us</span>
    </div>
  </div>
</section>

<section class="blog">
  <h2 class="heading">Latest Blog</h2>
  <article class="post post-1">
    <div class="post-image" role="img" aria-label="Illustration of a hand touching a digital globe with shopping cart and travel icons"></div>
    <div class="post-body">
      <div class="post-date"><svg viewBox="0 0 26 26"><rect x="2" y="5" width="22" height="19" fill="none" stroke="#9aa0a8" stroke-width="2"/><line x1="2" y1="11" x2="24" y2="11" stroke="#9aa0a8" stroke-width="2"/><line x1="8" y1="2" x2="8" y2="7" stroke="#9aa0a8" stroke-width="2"/><line x1="18" y1="2" x2="18" y2="7" stroke="#9aa0a8" stroke-width="2"/></svg>15 Mar 2015</div>
      <h3>A handy Lorem Ipsum Generator that help to create dummy text for all layout needs.</h3>
      <div class="author">By Ellis Marsh</div>
      <p>Lorem ipsum dolor sit amet, nsectetur adipiscing elit, sed do eiusmod tempor incididunt ut labore empor incididunt ut dolore magna aliqua.</p>
    </div>
  </article>
  <article class="post post-2">
    <div class="post-image" role="img" aria-label="Illustration of a hand touching a digital globe with shopping cart and travel icons"></div>
    <div class="post-body">
      <div class="post-date"><svg viewBox="0 0 26 26"><rect x="2" y="5" width="22" height="19" fill="none" stroke="#9aa0a8" stroke-width="2"/><line x1="2" y1="11" x2="24" y2="11" stroke="#9aa0a8" stroke-width="2"/><line x1="8" y1="2" x2="8" y2="7" stroke="#9aa0a8" stroke-width="2"/><line x1="18" y1="2" x2="18" y2="7" stroke="#9aa0a8" stroke-width="2"/></svg>15 Mar 2015</div>
      <h3>A handy Lorem Ipsum Generator that help to create dummy text for all layout needs.</h3>
      <div class="author">By Ellis Marsh</div>
      <p>Lorem ipsum dolor sit amet, nsectetur adipiscing elit, sed do eiusmod tempor incididunt ut labore empor incididunt ut dolore magna aliqua.</p>
    </div>
  </article>
  <article class="post post-3">
    <div class="post-image" role="img" aria-label="Illustration of a hand touching a digital globe with shopping cart and travel icons"></div>
    <div class="post-body">
      <div class="post-date"><svg viewBox="0 0 26 26"><rect x="2" y="5" width="22" height="19" fill="none" stroke="#9aa0a8" stroke-width="2"/><line x1="2" y1="11" x2="24" y2="11" stroke="#9aa0a8" stroke-width="2"/><line x1="8" y1="2" x2="8" y2="7" stroke="#9aa0a8" stroke-width="2"/><line x1="18" y1="2" x2="18" y2="7" stroke="#9aa0a8" stroke-width="2"/></svg>15 Mar 2015</div>
      <h3>A handy Lorem Ipsum Generator that help to create dummy text for all layout needs.</h3>
      <div class="author">By Ellis Marsh</div>
      <p>Lorem ipsum dolor sit amet, nsectetur adipiscing elit, sed do eiusmod tempor incididunt ut labore empor incididunt ut dolore magna aliqua.</p>
    </div>
  </article>
</section>

<footer class="site-footer">
  <h2 class="heading">Get in Touch</h2>
  <p class="address">228, Lorem Ipsum dolor sit,<br>litmus alusa - 859854</p>
  <div class="footer-phone">0800 555 0142</div>
  <div class="footer-email">info@northfieldservercrate.com</div>
  <div class="social" aria-label="Social links"><i></i><i></i><i></i></div>
  <p class="copyright">Copyright © 2015 Northfield Server Crate<br>All Rights Reserved</p>
</footer>

</body>
</html>
```